Lantern Square, Steady Course. (Website Design)

We are launching a new bipartisan civic movement: Lantern Square. Steady Course.
The mission is this: Americans deserve a government that is legally required to serve them honestly.
We are looking for a world-class website designer capable of creating an emotionally powerful, modern, cinematic landing page experience that feels larger than politics.
This is not a campaign website for a political party or candidate. We are not looking for a red, white, and blue page with stripes, or American flags, or stock footage of smiling people in a voting booth. We are looking for an emotional and cinematic experience through and through.
The visual direction should feel:
Historic
Hopeful
American
Emotional
Cinematic
Trustworthy
Timeless
The goal is to make visitors feel that they are witnessing the beginning of something important and want to be part of it in the end.
Primary Objective:
Inspire visitors to participate in a one-minute survey and cast their vote.
The survey itself is extremely short and takes approximately one minute to complete.
Everything on the page should ultimately guide visitors toward this action while creating enough curiosity, trust, emotional engagement, and excitement that they feel compelled to take part in the movement.
Audience:
The audience is ordinary Americans across the political spectrum: Democrats, Republicans, Independents.
The design should feel unifying and welcoming.
It should avoid looking partisan, ideological, activist, or government-issued.
Creative Freedom:
We are intentionally giving designers substantial creative freedom.
We are not looking for someone to simply arrange content into predefined sections.
Instead, we are looking for a designer who can think strategically about user experience and persuasion.
The ideal design is as minimal as possible, but you may always:
Use as many sections as you believe are necessary.
Use as many images as you believe are necessary.
Include storytelling elements.
Include data visualizations.
Include timelines.
Include videos.
Include animations.
Include or exclude sections as you see fit.
Reorganize the flow entirely.
We uploaded some files containing text and section suggestions. You don’t have to use them.
We also uploaded some images to convey the general feel we’re looking for.
We are much more interested in the effectiveness of the overall experience than in any specific layout.
What success looks like:
Think outside the box.
Please do not create another generic political website. We have already explored those approaches.
We are looking for something different.
The winning design will be the one that most effectively guides visitors from curiosity to belief to participation.
When a visitor reaches the end of the experience, they should feel:
This is bigger than politics.
This is something I can support regardless of party.
This feels credible.
This feels hopeful.
I want to be part of this.
Use the survey results, the research findings, the principles, the storytelling, or any other elements you believe will help build trust and inspire participation.
Don't just impress us with flashy visuals. Impress us with a website experience that inspires people to become part of the movement and cast their vote.
The final call-to-action should feel like the natural conclusion of the journey, not a request for engagement.
Our goal is not simply to inform visitors. Our goal is to inspire them to cast their vote.
Prioritize emotional impact, storytelling, clarity, and persuasion over decorative design elements.
Final words:
Design a website experience that successfully inspires visitors to take the survey and cast their vote.
Think like a storyteller, not just a designer.
Thank you for your interest in the project.
Best of luck.

```html
<!DOCTYPE html>
<html lang="en">
<head>
<meta charset="utf-8">
<title>Lantern Square. Steady Course.</title>
<link href="https://fonts.googleapis.com/css2?family=Playfair+Display:ital,wght@0,400;0,500;0,700;1,400;1,500&family=Nunito+Sans:wght@400;600;700&display=swap" rel="stylesheet">
<style>
:root{
  --navy:#0a1f5c;
  --navy-deep:#071544;
  --navy-card:#0d2a6e;
  --red:#d3121a;
  --ice:#eef3f7;
  --ink:#22304f;
  --muted:#5b6580;
  --white:#ffffff;
}
*{box-sizing:border-box;margin:0;padding:0}
html,body{width:1200px;height:3699px;overflow:hidden}
body{font-family:"Nunito Sans",Arial,sans-serif;color:var(--ink);background:var(--white);position:relative}
section,footer{position:relative;width:1200px;overflow:hidden}
.abs{position:absolute}

/* Hero */
.hero{height:474px;background:var(--navy-deep)}
.hero-media{position:absolute;inset:0;background:
  radial-gradient(ellipse 220px 260px at 310px 150px,#6b5440 0%,rgba(60,45,35,.6) 50%,transparent 100%),
  radial-gradient(ellipse 140px 170px at 1035px 200px,#a78670 0%,rgba(90,70,60,.5) 55%,transparent 100%),
  radial-gradient(ellipse 120px 70px at 680px 90px,#6e2a3a 0%,transparent 100%),
  linear-gradient(180deg,#2c2b33 0%,#1b2546 55%,#0d1a44 100%)}
.hero-shade{position:absolute;inset:0;background:linear-gradient(180deg,rgba(8,18,50,.2) 0%,rgba(8,18,50,.35) 55%,rgba(8,18,50,.85) 100%)}
.logo{font-family:"Playfair Display",Georgia,serif;font-weight:700;font-size:13px;line-height:14px;letter-spacing:.3px;text-transform:uppercase}
.hero .logo{left:171px;top:11px;color:var(--white)}
.nav{top:16px;left:600px}
.nav a{color:var(--white);text-decoration:none;font-size:11px;font-weight:600;letter-spacing:.3px;text-transform:uppercase}
.nav .n1{position:absolute;left:9px;top:8px}
.nav .n2{position:absolute;left:86px;top:8px}
.nav .n3{position:absolute;left:169px;top:8px}
.nav .n4{position:absolute;left:261px;top:8px}
.btn-red{background:var(--red);color:var(--white);text-transform:uppercase;font-weight:600;font-size:11px;display:flex;align-items:center;justify-content:center;text-decoration:none}
.nav .vote{position:absolute;left:334px;top:0;width:94px;height:30px;white-space:nowrap}
.hero h1{left:171px;top:268px;color:var(--white);font-family:"Playfair Display",Georgia,serif;font-weight:400;font-size:55px;line-height:54px}
.hero h1 em{font-style:italic}
.watch{left:171px;top:404px;display:flex;align-items:center;gap:14px;color:var(--white);font-size:11px;font-weight:600;letter-spacing:1.6px;text-transform:uppercase}
.watch .ring{width:37px;height:37px;border:1.5px solid var(--white);border-radius:50%;display:flex;align-items:center;justify-content:center}

/* Mission */
.mission{height:305px;background:
  radial-gradient(ellipse 420px 200px at 260px 60px,rgba(168,226,230,.75),transparent 70%),
  radial-gradient(ellipse 520px 230px at 1050px 290px,rgba(208,190,236,.8),transparent 70%),
  #f1f4f8;text-align:center}
.eyebrow{color:var(--red);font-size:11px;font-weight:600;letter-spacing:.4px;text-transform:uppercase}
.mission .eyebrow{position:absolute;top:58px;width:100%}
.mission .lead{position:absolute;top:88px;width:100%;font-family:"Playfair Display",Georgia,serif;font-size:20.5px;line-height:29px;color:#1a2140}
.mission .ask{position:absolute;top:157px;width:100%;font-family:"Playfair Display",Georgia,serif;font-size:20.5px;line-height:29px;color:#2a3f9a}
.mission .note{position:absolute;top:226px;width:100%;font-size:12.5px;color:#3b4258}

/* Who we are */
.who{height:442px;background:var(--navy)}
.who h2{left:171px;top:70px;color:var(--white);font-family:"Playfair Display",Georgia,serif;font-weight:500;font-size:32px;letter-spacing:.2px}
.who .sub{left:171px;top:120px;width:380px;color:var(--white);font-family:"Playfair Display",Georgia,serif;font-size:20.5px;line-height:29px}
.who .copy{left:171px;top:196px;width:365px;color:var(--white);font-size:12.5px;line-height:20.5px}
.who .copy p+p{margin-top:12px}
.photo{position:absolute;background:linear-gradient(135deg,#6c6f78,#2d3038)}
.photo.warm{background:linear-gradient(135deg,#9b7a5e,#3d342e)}
.photo.blue{background:linear-gradient(135deg,#587294,#1e2a44)}

/* Journey */
.journey{height:829px;background:var(--ice)}
.journey h2{top:54px;width:100%;text-align:center;font-family:"Playfair Display",Georgia,serif;font-weight:500;font-size:32px;color:#1a2140}
.spine{left:599px;top:171px;width:2px;height:549px;background:#2b3f7d}
.node{position:absolute;left:570px;width:62px;height:62px;border-radius:50%;background:var(--ice);border:1.5px solid #2b3f7d;display:flex;align-items:center;justify-content:center;margin-top:-31px}
.node.final{background:var(--red);border-color:var(--red);box-shadow:0 0 0 4px var(--ice),0 0 0 5.5px #2b3f7d}
.step{position:absolute;width:306px;height:91px;background:var(--navy);color:var(--white);font-size:13px;line-height:21px;display:flex;align-items:center}
.step.right{left:623px;clip-path:polygon(3% 0,100% 0,97% 100%,0 100%);padding:0 34px 0 26px}
.step.left{left:271px;clip-path:polygon(0 0,97% 0,100% 100%,3% 100%);padding:0 26px 0 34px;text-align:right;justify-content:flex-end}
.tag{position:absolute;height:20px;background:var(--red);color:var(--white);font-size:11px;font-weight:600;text-transform:uppercase;display:flex;align-items:center;padding:0 12px;clip-path:polygon(6% 0,100% 0,100% 100%,0 100%)}

/* Principles */
.principles{height:522px;background:
  radial-gradient(ellipse 380px 260px at 140px 120px,rgba(110,30,90,.85),transparent 70%),
  radial-gradient(ellipse 460px 300px at 1080px 90px,rgba(40,70,160,.55),transparent 70%),
  linear-gradient(180deg,#1a1d5a 0%,#0e2564 100%)}
.principles h2{top:54px;width:100%;text-align:center;font-family:"Playfair Display",Georgia,serif;font-weight:500;font-size:32px;color:var(--white)}
.card{position:absolute;width:205px;border:1px solid rgba(255,255,255,.18);color:var(--white);font-size:12.5px;line-height:19px;text-align:center;padding:36px 22px 0}
.badge{position:absolute;left:50%;top:-15px;margin-left:-15px;width:30px;height:30px;border-radius:50%;background:var(--red);color:var(--white);font-family:"Playfair Display",Georgia,serif;font-size:17px;display:flex;align-items:center;justify-content:center}
.card .big{font-family:"Playfair Display",Georgia,serif;font-size:50px;line-height:56px;margin-top:-6px}

/* Survey */
.survey{height:608px;background:var(--white)}
.survey-band{left:0;top:63px;width:893px;height:351px;border-radius:0 10px 0 0;background:
  radial-gradient(ellipse 300px 260px at 720px 80px,rgba(30,40,120,.9),transparent 70%),
  radial-gradient(ellipse 360px 300px at 420px 120px,rgba(200,20,30,.95),transparent 75%),
  linear-gradient(160deg,#2a1c5e 0%,#b3121c 55%,#d3121a 100%)}
.survey h2{left:171px;top:96px;color:var(--white);font-family:"Playfair Display",Georgia,serif;font-weight:500;font-size:32px}
.survey .stat{left:171px;top:152px;color:var(--white);font-family:"Playfair Display",Georgia,serif;font-size:25px}
.survey .stat-note{left:171px;top:190px;width:185px;color:var(--white);font-size:13px;line-height:19px}
.survey .aside{left:364px;top:190px;width:380px;color:var(--white);font-size:12.5px;line-height:19px;border-left:1px solid rgba(255,255,255,.5);padding-left:13px}
.panel{left:171px;top:264px;width:857px;height:282px;border-radius:8px;background:linear-gradient(90deg,#cfe6f4 0%,#e8f1f6 50%,#d6eae2 100%)}
.tile{position:absolute;background:var(--white);border-radius:6px;font-size:12.5px;line-height:17px;color:#3a4358}
.figure{font-family:"Playfair Display",Georgia,serif;font-size:20px;color:var(--navy)}
.figcap{font-size:12px;color:#2a4aa8;white-space:nowrap}
.tick{color:var(--red);font-weight:700;margin-right:4px}

/* Call to action */
.cta{height:371px;background:
  radial-gradient(ellipse 360px 260px at 880px 170px,#3f6fd6 0%,rgba(40,80,190,.6) 45%,transparent 80%),
  linear-gradient(180deg,#123a94 0%,#1a4aa8 50%,#0d2a78 100%)}
.cta h2{left:171px;top:62px;color:var(--white);font-family:"Playfair Display",Georgia,serif;font-weight:500;font-size:32px}
.cta .body{left:171px;top:118px;width:440px;color:var(--white);font-size:12.5px;line-height:17px}
.cta .bold{left:171px;top:187px;color:var(--white);font-size:13.5px;font-weight:600}
.cta .small{left:171px;top:226px;color:var(--white);font-size:12.5px}
.cta .go{left:171px;top:265px;width:181px;height:36px;gap:8px}
.counter{left:787px;top:83px;width:192px;height:202px;background:rgba(20,50,130,.75);border:1px solid rgba(255,255,255,.3);border-radius:3px;text-align:center;color:var(--white)}
.counter .ico{width:44px;height:44px;border-radius:50%;background:var(--red);margin:22px auto 0;display:flex;align-items:center;justify-content:center}
.counter .num{font-family:"Playfair Display",Georgia,serif;font-size:38px;margin-top:12px;line-height:44px}
.counter .lbl{font-size:13px;line-height:19px;margin-top:4px}

/* Footer */
.site-footer{height:148px;background:var(--white)}
.site-footer .logo{left:171px;top:29px;color:var(--navy)}
.foot-links a{position:absolute;top:33px;font-size:11.5px;color:var(--navy);text-decoration:none;text-transform:uppercase}
.social{position:absolute;top:32px;display:flex;align-items:center;gap:6px;font-size:12px;color:var(--navy)}
.social i{display:block;width:10px;height:10px;border-radius:50%;background:var(--navy)}
.rule{left:0;top:95px;width:1200px;height:1px;background:#e1e5ee}
.copyright{top:111px;width:100%;text-align:center;font-size:11.5px;color:#3a4358}
</style>
</head>
<body>

<section class="hero">
  <div class="hero-media" role="img" aria-label="Cinematic collage of a historic statesman's portrait, a waving national flag and a smiling young woman"></div>
  <div class="hero-shade"></div>
  <div class="logo abs">Lantern Square<br>Steady Course</div>
  <nav class="nav abs">
    <a class="n1" href="#mission">Mission</a>
    <a class="n2" href="#journey">Journey</a>
    <a class="n3" href="#principles">Principles</a>
    <a class="n4" href="#survey">Survey</a>
    <a class="vote btn-red" href="#vote">Vote Now</a>
  </nav>
  <h1 class="abs">A Government That Serves<br>The People <em>Honestly</em></h1>
  <div class="watch abs">
    <span class="ring"><svg width="12" height="13" viewBox="0 0 12 13"><path d="M2 1 L11 6.5 L2 12 Z" fill="#fff"/></svg></span>
    Watch the video
  </div>
</section>

<section class="mission" id="mission">
  <p class="eyebrow">Mission Statement</p>
  <p class="lead">Today, not a single law binds our government<br>to act honestly, and in our best interest.</p>
  <p class="ask">If our government exists solely to serve us,<br>Why isn’t it legally required to?</p>
  <p class="note">We founded this movement to change that.</p>
</section>

<section class="who">
  <svg class="abs" style="left:0;top:0" width="1200" height="442" viewBox="0 0 1200 442">
    <polygon points="1070,0 1110,0 830,442 790,442" fill="#12307a"/>
    <polygon points="640,150 700,150 560,442 500,442" fill="#12307a"/>
    <polygon points="880,200 960,40 1010,40 930,200" fill="#163784"/>
  </svg>
  <h2 class="abs">WHO WE ARE</h2>
  <p class="sub abs">We are a bipartisan movement based in Washington, D.C.</p>
  <div class="copy abs">
    <p>We believe Americans deserve a government legally required to act honestly, transparently, and in the public’s best interest.</p>
    <p>At a time of growing division and distrust,<br>we are working to unite Americans around a simple idea: government should faithfully serve the people, not special interests.</p>
  </div>
  <div class="photo" style="left:659px;top:21px;width:120px;height:121px" role="img" aria-label="Archival photo of a civil rights speaker"></div>
  <div class="photo warm" style="left:785px;top:21px;width:125px;height:121px" role="img" aria-label="Archival photo of a civil rights leader"></div>
  <div class="photo" style="left:916px;top:21px;width:112px;height:121px" role="img" aria-label="Archival photo of a civil rights activist"></div>
  <div class="photo blue" style="left:558px;top:148px;width:130px;height:150px" role="img" aria-label="Archival photo of a mid-century president"></div>
  <div class="photo" style="left:693px;top:148px;width:178px;height:150px" role="img" aria-label="Archival photo of marchers holding protest signs"></div>
  <div class="photo warm" style="left:877px;top:148px;width:128px;height:150px" role="img" aria-label="Photo of a footprint on the lunar surface"></div>
  <div class="photo" style="left:538px;top:305px;width:104px;height:117px" role="img" aria-label="Archival photo of the Capitol dome"></div>
  <div class="photo warm" style="left:649px;top:305px;width:120px;height:117px" role="img" aria-label="Archival photo of a speaker before a vast crowd"></div>
  <div class="photo" style="left:775px;top:305px;width:111px;height:117px" role="img" aria-label="Archival photo of a civil rights march banner"></div>
</section>

<section class="journey" id="journey">
  <h2 class="abs">OUR JOURNEY</h2>
  <div class="spine abs"></div>

  <div class="node" style="top:171px"><svg width="26" height="26" viewBox="0 0 26 26" fill="none" stroke="#d3121a" stroke-width="1.4"><path d="M13 4a7 7 0 0 0-4 12.7V19h8v-2.3A7 7 0 0 0 13 4z"/><path d="M10 21.5h6M11 24h4M13 1v1.5M4 5l1 1M22 5l-1 1"/></svg></div>
  <div class="node" style="top:309px"><svg width="26" height="26" viewBox="0 0 26 26" fill="none" stroke="#d3121a" stroke-width="1.6"><circle cx="11" cy="11" r="7"/><path d="M16 16l7 7"/></svg></div>
  <div class="node" style="top:445px"><svg width="24" height="26" viewBox="0 0 24 26" fill="none" stroke="#d3121a" stroke-width="1.4"><rect x="4" y="2" width="16" height="22" rx="1.5"/><path d="M8 8h8M8 12h8M8 16h8M8 20h5"/></svg></div>
  <div class="node" style="top:583px"><svg width="26" height="26" viewBox="0 0 26 26" fill="none" stroke="#d3121a" stroke-width="1.4"><rect x="6" y="3" width="15" height="20" rx="1.5"/><path d="M10 8h7M10 12h7M10 16h4"/><circle cx="6" cy="20" r="4"/><path d="M4.3 20l1.2 1.2 2.2-2.4"/></svg></div>
  <div class="node final" style="top:720px"><svg width="28" height="24" viewBox="0 0 28 24" fill="none" stroke="#fff" stroke-width="1.4"><rect x="2" y="2" width="24" height="19"/><path d="M6 17v-5M10 17v-8M14 17v-6M18 17v-9M22 17v-4M5 10l5-4 4 3 4-4 5 3"/></svg></div>

  <span class="tag" style="left:640px;top:118px">August 2024</span>
  <div class="step right" style="top:138px">We turned those principles into a rigorous framework and named it Lantern Square, Steady Course.</div>

  <span class="tag" style="left:462px;top:255px">October 2025</span>
  <div class="step left" style="top:275px">We identified 10 principles that most of Americans agree our government must uphold.</div>

  <span class="tag" style="left:640px;top:391px">March 2026</span>
  <div class="step right" style="top:411px">We turned those principles into a rigorous framework and named it Lantern Square, Steady Course.</div>

  <span class="tag" style="left:468px;top:529px">April 2026</span>
  <div class="step left" style="top:549px">We tested the framework in a pre-registered national study with Americans across the political spectrum.</div>

  <div class="step right" style="top:675px">And the results exceeded all our expectation.</div>
</section>

<section class="principles" id="principles">
  <h2 class="abs">THE SEVEN PRINCIPLES</h2>
  <div class="card" style="left:171px;top:138px;height:140px"><span class="badge">1</span>Public officials should only serve the public good. Not private interests.</div>
  <div class="card" style="left:389px;top:138px;height:140px"><span class="badge">2</span>Major government decisions should be based on truth, and rigorous evidence. Not party loyalty, pressure, or donors.</div>
  <div class="card" style="left:607px;top:138px;height:140px"><span class="badge">3</span>When a public decision is made, people should be able to see the reasoning. Clearly. Honestly. On the record.</div>
  <div class="card" style="left:825px;top:138px;height:140px;width:203px"><span class="badge">4</span>And if the government reasoning is flawed, citizens should have a way to challenge it, And get a real response.</div>
  <div class="card" style="left:171px;top:316px;height:143px"><span class="badge">5</span>Conflicts of interest in public office all should be disclosed, Before decisions are made.</div>
  <div class="card" style="left:389px;top:316px;height:143px;padding-top:40px"><span class="badge">6</span>Lying or misleading the public in official decisions should carry consequences. Real ones.</div>
  <div class="card" style="left:607px;top:316px;height:143px;padding-top:40px"><span class="badge">7</span>And most importantly, Money should never outweigh people’s voice.</div>
  <div class="card" style="left:825px;top:316px;height:143px;width:203px;padding-top:30px"><div class="big">89.9%*</div>Said Agree.</div>
</section>

<section class="survey" id="survey">
  <div class="survey-band abs"></div>
  <h2 class="abs">THE SURVEY</h2>
  <p class="stat abs">82.9%*</p>
  <p class="stat-note abs">of Americans said YES on a state ballot vote.</p>
  <p class="aside abs">We conducted a pre-registered national study with X number<br>Americans across the political spectrum.</p>

  <div class="panel abs">
    <div class="tile" style="left:20px;top:20px;width:369px;height:94px;display:flex;align-items:center;padding:0 16px;gap:12px">
      <svg width="24" height="30" viewBox="0 0 24 30" fill="none" stroke="#d3121a" stroke-width="1.4"><rect x="2" y="4" width="20" height="24" rx="1.5"/><rect x="8" y="1.5" width="8" height="5" rx="1"/><path d="M6 13l2 2 3-3M13 14h6M6 20l2 2 3-3M13 21h6"/></svg>
      <span style="width:200px;font-size:12px;white-space:nowrap">We first laid out the 7 principles.<br>We asked if they agree?</span>
      <span><span class="figure">89.9%*</span><br><span class="figcap">Said they Agree.</span></span>
    </div>
    <div class="tile" style="left:20px;top:122px;width:369px;height:140px;padding:18px 16px 0">
      <p>Then we asked:<br>Would you support a legal framework built around them?</p>
      <div style="display:flex;margin-top:14px;align-items:flex-end">
        <div style="width:82px;border-right:1px solid #d8dce6;padding-top:16px"><span class="figure">82.9%*</span><br><span class="figcap">Said yes.</span></div>
        <div style="width:126px;padding-left:10px;border-right:1px solid #d8dce6;padding-top:16px"><span class="figure">14.4%*</span><br><span class="figcap">Remained neutral.</span></div>
        <div style="padding-left:10px"><span class="figcap">Only</span><br><span class="figure">82.9%*</span><br><span class="figcap">Actively opposed it.</span></div>
      </div>
    </div>
    <div class="tile" style="left:399px;top:20px;width:258px;height:242px;padding:14px 16px 0">
      <div style="display:flex;gap:12px">
        <svg width="28" height="26" viewBox="0 0 28 26" fill="none" stroke="#d3121a" stroke-width="1.3"><path d="M14 2v21M8 23h12M4 6h20M4 6l-3 8h6zM24 6l-3 8h6zM1 14a3 3 0 0 0 6 0M21 14a3 3 0 0 0 6 0"/></svg>
        <p style="font-size:12px;line-height:16px">But broad support is easy when ideas stay vague. So we stress-tested it.</p>
      </div>
      <p style="font-size:12px;line-height:16px;margin:6px 0 0 40px">We showed participants the full framework.</p>
      <p style="margin-top:8px;font-size:12px;line-height:20px"><span class="tick">✓</span>The legal structure.<br><span class="tick">✓</span>The enforcement model.<br><span class="tick">✓</span>The actual mechanism.</p>
      <p style="margin-top:6px;font-size:12px;line-height:17px">Most reforms lose support once the details appear. This one didn’t. Support held.</p>
    </div>
    <div class="tile" style="left:666px;top:20px;width:172px;height:242px;padding:16px 16px 0">
      <svg width="32" height="30" viewBox="0 0 32 30" fill="none" stroke="#d3121a" stroke-width="1.4"><circle cx="12" cy="9" r="6"/><path d="M2 28c0-6 4-10 10-10s10 4 10 10z"/><circle cx="23" cy="8" r="4.5"/><path d="M24 16c4 0 7 3 7 8h-6"/></svg>
      <div style="margin-top:10px;background:linear-gradient(90deg,#f3f5f9,#fff);padding:2px 0 2px 8px"><span class="figcap">Democrats</span><br><span class="figure">84.5%*</span></div>
      <div style="margin-top:6px;background:linear-gradient(90deg,#f3f5f9,#fff);padding:2px 0 2px 8px"><span class="figcap">Republicans</span><br><span class="figure">80.2%*</span></div>
      <div style="margin-top:6px;background:linear-gradient(90deg,#f3f5f9,#fff);padding:2px 0 2px 8px"><span class="figcap">Independants</span><br><span class="figure">79.9%*</span></div>
      <p style="margin-top:8px;font-size:12px;padding-left:2px">They all said, YES.</p>
    </div>
  </div>
</section>

<section class="cta" id="vote">
  <div class="abs" style="inset:0" role="img" aria-label="Aerial view of a vast crowd of people gathered in a blue-toned square"></div>
  <h2 class="abs">BE PART OF HISTORY. VOTE NOW.</h2>
  <p class="body abs">For decades, we have argued over policies, parties, and ideologies.<br>But today, across political lines, generations, and races,<br>Americans are arriving at the same conclusion:</p>
  <p class="bold abs">We deserve a government legally required to serve the people honestly.</p>
  <p class="small abs">And we don’t have to ask for it. We just have to vote for it.</p>
  <a class="go btn-red abs" href="#vote">Cast Your Vote Now
    <svg width="12" height="10" viewBox="0 0 12 10" fill="none" stroke="#fff" stroke-width="1.6"><path d="M0 5h10M6 1l4 4-4 4"/></svg></a>
  <div class="counter abs">
    <div class="ico"><svg width="26" height="22" viewBox="0 0 26 22" fill="none" stroke="#fff" stroke-width="1.4"><circle cx="13" cy="6" r="4"/><circle cx="5" cy="8" r="3"/><circle cx="21" cy="8" r="3"/><path d="M6 21c0-5 3-8 7-8s7 3 7 8zM1 20c0-4 2-6 4-6M25 20c0-4-2-6-4-6"/></svg></div>
    <div class="num">1016</div>
    <p class="lbl">People<br>Already Voted YES for<br>the Ballot</p>
  </div>
</section>

<footer class="site-footer">
  <div class="logo abs">Lantern Square<br>Steady Course</div>
  <nav class="foot-links">
    <a style="left:406px" href="#mission">Mission</a>
    <a style="left:484px" href="#journey">Journey</a>
    <a style="left:566px" href="#principles">Principles</a>
    <a style="left:659px" href="#survey">Survey</a>
    <a style="left:731px" href="#vote">Vote Now</a>
  </nav>
  <span class="social" style="left:854px"><i></i>Townsquare</span>
  <span class="social" style="left:953px"><i></i>Lenscast</span>
  <div class="rule abs"></div>
  <p class="copyright abs">© Copyright 2026 &nbsp;Lantern Square. Steady Course. All Rights Reserved</p>
</footer>

</body>
</html>
```